Emergency Vehicle Installer and Security Firm Needs a Business Card

Our company "Corvalt" need a business card for our Emergency Vehicle Equipment Installation and Infrastructure Security Business. We are contract designers, manufacturers and installers for Emergency Vehicle Fleets. This includes installation of Emergency Lights, Sirens, Vehicle Graphics and Radio Communications. We also supply this products to an international market. We also do consultant, and installation of high level security access, alarm and surveillance equipment for medium to large size businesses.

The design should represent a level of trust in our professionalism and expertise. It should visually display our ongoing relationship with the emergency services, but not overtake our commitment to high level security options.

Target Market(s)

Emergency Services and Businesses requiring high level security

Industry/Entity Type

Business

Contact Information for Business Card

*note complete details will be given to the winning designer for revising. The name "Mark Pell will be used to fill in name".

Mark Pell
Managing Director
Corvalt NZ Limited
Phone: +64 027 604 91352
Email: mark.pell@corvalt-example.co.nz

Requirements
Must have
• Card must be in black. Using our logo on the top as supplied. Designers should try having the reverse side as a blurred image of police lights (red and blue) with our logo in greyscale in the centre (this is not particularly a requirement, but feel free to play around with this option).
Nice to have
• A card design that looks good when spot UV printed. A clean compact and graphic design. A grey scale feel on the front (excluding logo, but you can play around with that idea). Rounded smooth text.
Should not have
• Will update this section as designs come through - feel free to submit what you feel would look good.

```html
<!DOCTYPE html>
<html lang="en">
<head>
<meta charset="utf-8">
<title>Corvalt NZ Limited – Business Card</title>
<link rel="stylesheet" href="https://fonts.googleapis.com/css2?family=Arimo:wght@400;700&display=swap">
<style>
  :root {
    --page: #ecebe8;
    --card-grey: #a9a9a9;
    --band-black: #1e1b1a;
    --brand-red: #d8261f;
    --ink: #1c1c1c;
    --shadow: rgba(0, 0, 0, 0.22);
  }
  * { box-sizing: border-box; margin: 0; padding: 0; }
  html, body {
    width: 1200px;
    height: 1200px;
    overflow: hidden;
    background: var(--page);
    font-family: "Arimo", Arial, sans-serif;
    color: var(--ink);
  }
  .sheet {
    position: relative;
    width: 1200px;
    height: 1200px;
  }
  .card {
    position: absolute;
    width: 660px;
    height: 390px;
    background: var(--card-grey);
    box-shadow: 0 6px 18px var(--shadow);
    overflow: hidden;
  }
  /* Front side */
  .card--front { left: 110px; top: 120px; }
  .front__band {
    height: 180px;
    background: var(--band-black);
    display: flex;
    align-items: flex-end;
    justify-content: center;
    padding-bottom: 26px;
    padding-left: 50px;
  }
  .front__company {
    color: var(--brand-red);
    font-size: 38px;
    font-weight: 400;
    letter-spacing: 0.2px;
  }
  .front__details {
    position: relative;
    height: 210px;
  }
  .person {
    position: absolute;
    left: 150px;
    top: 40px;
    text-align: center;
    width: 190px;
  }
  .person__name { font-size: 30px; font-weight: 400; }
  .person__title { font-size: 17px; margin-top: 4px; }
  .divider {
    position: absolute;
    left: 395px;
    top: 26px;
    width: 3px;
    height: 48px;
    background: var(--brand-red);
  }
  .contact {
    position: absolute;
    left: 430px;
    top: 18px;
    list-style: none;
    font-size: 17px;
  }
  .contact__item {
    display: flex;
    align-items: center;
    gap: 9px;
    height: 28px;
  }
  .contact__icon { width: 16px; height: 16px; flex: none; }
  /* Back side */
  .card--back {
    left: 430px;
    top: 680px;
    display: flex;
    align-items: center;
    justify-content: center;
  }
  .back__wordmark {
    display: flex;
    align-items: center;
    gap: 14px;
  }
  .back__mark {
    width: 34px;
    height: 34px;
    border-radius: 50%;
    background: var(--brand-red);
  }
  .back__name {
    font-size: 62px;
    font-weight: 700;
    color: var(--band-black);
    letter-spacing: 1px;
    text-transform: uppercase;
  }
</style>
</head>
<body>
<main class="sheet">
  <section class="card card--front" aria-label="Business card front">
    <header class="front__band">
      <h1 class="front__company">Corvalt NZ Limited</h1>
    </header>
    <div class="front__details">
      <div class="person">
        <p class="person__name">Mark Pell</p>
        <p class="person__title">Managing Director</p>
      </div>
      <span class="divider"></span>
      <ul class="contact">
        <li class="contact__item">
          <svg class="contact__icon" viewBox="0 0 16 16" aria-hidden="true">
            <circle cx="8" cy="8" r="7" fill="none" stroke="#1c1c1c" stroke-width="1.2"/>
            <path d="M5.3 4.6c.4-.4.9-.3 1.1.1l.6 1.2c.2.4 0 .7-.3 1l-.3.3c.4.9 1.2 1.7 2.1 2.1l.3-.3c.3-.3.6-.5 1-.3l1.2.6c.4.2.5.7.1 1.1-.7.8-1.8.9-2.8.3C6.8 10.1 5.9 9.2 5.1 7.7c-.6-1-.5-2.3.2-3.1z" fill="#1c1c1c"/>
          </svg>
          <span>+64 027 604 91352</span>
        </li>
        <li class="contact__item">
          <svg class="contact__icon" viewBox="0 0 16 16" aria-hidden="true">
            <rect x="1.5" y="3.5" width="13" height="9" fill="none" stroke="#1c1c1c" stroke-width="1.2"/>
            <path d="M1.5 3.5 8 9l6.5-5.5" fill="none" stroke="#1c1c1c" stroke-width="1.2"/>
          </svg>
          <span>mark.pell@corvalt-example.co.nz</span>
        </li>
      </ul>
    </div>
  </section>

  <section class="card card--back" aria-label="Business card back">
    <div class="back__wordmark">
      <span class="back__mark"></span>
      <span class="back__name">Corvalt</span>
    </div>
  </section>
</main>
</body>
</html>
```